Professional banners for an eyewear company

I have 3 images which need to be made into banners. Size 990 x 370, with a 10 pixel white border at top and bottom of banner.

They all need to be adjusted to make the colours better and less bright.
All will need some writing written on them with a nice serif font.

Banner 1 text: Handcrafted luxury eyewear, with a purpose...
Banner 2 text: Half of our profits go to help malnourished children in India
Banner 3 text: 10% of your first order, use code: First Order

On our homepage these 3 banners will alternate, so they need to look good together.

Tips
Please take a look at the banners on the lunvoreck.com homepage, this is kind of how I want the text to be displayed, and they use good colours.

The backgrounds on Banners 2 & 3 can be changed.
Banner 3 background if you can change to a nice colour, as per lunvoreck.com homepage.
Updates

Hi, just a quick update, thank you for all the designs submitted so far, please keep in mind that the brand is a luxury high-end brand so designs will need to reflect this.

Industry/Entity Type

Eyewear

```html
<!DOCTYPE html>
<html lang="en">
<head>
<meta charset="utf-8">
<title>Half of our profits – banner</title>
<link rel="stylesheet" href="https://fonts.googleapis.com/css2?family=Josefin+Sans:wght@200&family=Alegreya:wght@400&display=swap">
<style>
  :root {
    --page-white: #ffffff;
    --panel-olive: #a6b545;
    --panel-olive-deep: #95a538;
    --panel-lime: #cddb79;
    --panel-lime-light: #d5e186;
    --headline-cream: #f7f6c4;
    --copy-cream: #fbfbe6;
    --map-shade: rgba(120, 135, 40, 0.28);
    --photo-tone-top: #c3d36f;
    --photo-tone-bottom: #9cc441;
  }
  html, body {
    margin: 0;
    padding: 0;
    width: 1200px;
    height: 448px;
    overflow: hidden;
    background: var(--page-white);
  }
  .banner {
    position: absolute;
    top: 12px;
    left: 0;
    width: 1200px;
    height: 424px;
    display: flex;
  }
  .banner__message {
    position: relative;
    width: 605px;
    height: 100%;
    background: linear-gradient(180deg, var(--panel-olive) 0%, var(--panel-olive-deep) 100%);
    overflow: hidden;
  }
  .banner__map {
    position: absolute;
    left: 160px;
    top: 14px;
    width: 340px;
    height: 400px;
    background: radial-gradient(ellipse at 50% 45%, var(--map-shade) 0%, rgba(120,135,40,0) 70%);
  }
  .banner__headline {
    position: absolute;
    left: 0;
    width: 100%;
    top: 46px;
    margin: 0;
    text-align: center;
    font-family: "Josefin Sans", sans-serif;
    font-weight: 200;
    font-size: 150px;
    line-height: 150px;
    letter-spacing: -2px;
    color: var(--headline-cream);
  }
  .banner__copy {
    position: absolute;
    left: 0;
    width: 100%;
    top: 219px;
    margin: 0;
    text-align: center;
    font-family: "Alegreya", serif;
    font-size: 41px;
    line-height: 51px;
    color: var(--copy-cream);
  }
  .banner__visual {
    position: relative;
    flex: 1;
    height: 100%;
    background: linear-gradient(180deg, var(--panel-lime-light) 0%, var(--panel-lime) 100%);
    overflow: hidden;
  }
  .banner__photo {
    position: absolute;
    left: 122px;
    top: 15px;
    width: 358px;
    height: 409px;
    background: linear-gradient(180deg, var(--photo-tone-top) 0%, var(--photo-tone-bottom) 100%);
  }
</style>
</head>
<body>
  <section class="banner">
    <div class="banner__message">
      <div class="banner__map" role="img" aria-label="Faint map outline of India"></div>
      <h1 class="banner__headline">HALF</h1>
      <p class="banner__copy">of our profits go to help<br>malnourished children in India.</p>
    </div>
    <div class="banner__visual">
      <div class="banner__photo" role="img" aria-label="Photograph of a smiling young girl in a green top, resting her chin on her hand"></div>
    </div>
  </section>
</body>
</html>
```